Website For Custom Home Builder

-Very elegant and simple design as I am a high end custom home builder.
-I build homes $2 million to $10 million range so the website needs to reflect the level of home that I build.
-Attached are photos of homes I have built to use as well as my logo.
-I need final design to be in layered format so my local guy can edit if he needs to.

3 Page Design
1. HomePage:
-logo, some photos,
-“Building beautiful custom homes in Indianapolis for over 20 years”
2. AboutPage:
-Wade Holloran has been building stunning custom homes in the Indianpolis area for over 20 years. As a small boutique building company we only build a handful of homes a year in order to offer our clients the personal attention that their homes deserve. It's this attention to detail that makes our client experience and final product something special and unique.
- family photo
3. ContactPage:
-office photo
-317-552-7190
-wade@whcrafted.com
-415 North Fernmill Rd, Suite 308, Carmel IN 46033

Target Market(s)

Very high end clients looking to build $2 million to $10 million homes.

Industry/Entity Type

Residential high end custom home builder/construction

Coding

Coded - Design and coding required

Number of Pages Required

3 page

Requirements
Must have
• Very simple and elegant design that represents the high end homes that I build.
Nice to have
Should not have
• Should NOT have a lot of clutter or be a very busy page from a design perspective.

```html
<!DOCTYPE html>
<html lang="en">
<head>
<meta charset="utf-8">
<title>Wade Holloran Custom Homes</title>
<link rel="stylesheet" href="https://fonts.googleapis.com/css2?family=Red+Hat+Display:wght@300;400;500&family=Inter:wght@400;500;600&display=swap">
<style>
:root{
  --paper:#f3f2f0;
  --ink:#1d1a18;
  --muted:#4a4440;
  --rust:#9b4a17;
  --copper:#b35f23;
  --ember:#5a2a0f;
  --deep:#3a1004;
  --night:#2b2624;
  --line:#cfcac5;
  --head:'Red Hat Display',sans-serif;
  --body:'Inter',sans-serif;
}
*{margin:0;padding:0;box-sizing:border-box}
html,body{width:1200px;height:4658px;overflow:hidden}
body{background:var(--paper);color:var(--ink);font-family:var(--body);position:relative}
.abs{position:absolute}
.ph{position:absolute}

/* nav */
.nav-links{left:195px;top:36px;display:flex;gap:20px;font-size:8px;font-weight:600;letter-spacing:.3px}
.brand{left:480px;top:22px;width:240px;text-align:center;font-family:var(--head);color:var(--ink)}
.brand .name{font-size:19px;font-weight:400;letter-spacing:1px;display:block;margin-top:22px}
.brand .sub{font-size:8px;letter-spacing:5px;display:block;margin-top:2px}
.brand .dot{width:22px;height:22px;border:1.5px solid var(--ink);display:block;margin:0 auto;position:absolute;left:109px;top:0}
.nav-projects{left:850px;top:40px;font-size:8px;font-weight:600}
.btn{display:inline-block;border-radius:30px;font-size:8px;font-weight:600;text-align:center;letter-spacing:.3px}
.nav-quote{left:912px;top:29px;width:93px;height:31px;line-height:31px;background:var(--ember);color:#fff}

/* hero */
.hero{left:49px;top:96px;width:1102px;height:430px;border-radius:30px;overflow:hidden;background:linear-gradient(100deg,#5a2a0f 0%,#7e3b12 45%,#b35f23 100%)}
.hero .ghost{left:165px;top:-10px;font-family:var(--head);font-size:120px;font-weight:400;color:transparent;-webkit-text-stroke:1px rgba(255,255,255,.25);white-space:nowrap}
.hero h1{left:144px;top:72px;font-family:var(--head);font-weight:300;font-size:48px;line-height:54px;color:#fff}
.hero p{left:146px;top:255px;width:340px;font-size:11.5px;line-height:20px;color:#f2e3d8}
.hero .b1{left:146px;top:323px;width:87px;height:31px;line-height:31px;background:#e4cdb9;color:var(--ember)}
.hero .b2{left:242px;top:323px;width:58px;height:31px;line-height:29px;border:1px solid #e4cdb9;color:#f2e3d8}
.hero .house{left:511px;top:39px;width:591px;height:391px;background:linear-gradient(180deg,#7a4a2a 0%,#2e2a28 55%,#3b3a34 100%)}

/* intro */
.intro-title{left:0;top:612px;width:1200px;text-align:center;font-family:var(--head);font-weight:400;font-size:36px;line-height:45px}
.intro-text{left:225px;top:722px;width:750px;text-align:center;font-size:14.5px;line-height:23px;color:var(--muted)}
.stat{top:818px}
.stat .v{font-family:var(--head);font-size:37px;font-weight:400;display:flex;align-items:center;gap:14px}
.stat .v:before{content:"";width:18px;height:2px;background:var(--copper)}
.stat .l{font-family:var(--head);font-size:19px;margin-top:6px;padding-left:32px}
.stat-div{top:812px;width:1px;height:90px;background:var(--line)}
.laptop{left:407px;top:940px;width:388px;height:433px;border-radius:12px;background:linear-gradient(160deg,#e9e6e3 0%,#c98a52 45%,#f3dccb 70%,#e8e6e4 100%)}
.ghost2{left:0;top:1195px;width:1200px;font-family:var(--head);font-size:128px;white-space:nowrap;color:transparent;-webkit-text-stroke:1px #c9c4bf;overflow:hidden}

/* projects */
.projects{left:0;top:1323px;width:1200px;height:864px;background:linear-gradient(135deg,#4a1608 0%,var(--deep) 30%,var(--deep) 100%)}
.projects h2{left:193px;top:120px;font-family:var(--head);font-weight:300;font-size:38px;line-height:44px;color:#8a4a22}
.arrow{top:154px;width:47px;height:47px;border-radius:50%}
.arrow.prev{left:902px;background:#e4cdb9}
.arrow.next{left:956px;background:var(--copper)}
.card{position:absolute}
.card .img{position:absolute;left:0;top:0}
.card .plus{position:absolute;width:18px;height:18px;background:#2a0b02;color:#fff;font-size:13px;line-height:18px;text-align:center}
.card .t{position:absolute;font-family:var(--head);font-size:17px;color:#fff;white-space:nowrap}
.card .s{position:absolute;font-size:10px;color:#d9c2b2;white-space:nowrap}

/* services */
.svc-bg{left:0;top:2187px;width:1200px;height:686px;background:linear-gradient(90deg,#e6e2de 0%,#f3f2f0 30%,#f3f2f0 70%,#e6e2de 100%)}
.svc-photo{left:213px;top:2298px;width:365px;height:434px;background:linear-gradient(160deg,#f1efec 0%,#d9b78d 50%,#b88755 100%)}
.svc-card{left:551px;top:2345px;width:437px;height:353px;background:#fff;box-shadow:0 8px 30px rgba(0,0,0,.08)}
.svc-card h2{position:absolute;left:30px;top:28px;font-family:var(--head);font-weight:300;font-size:36px;line-height:43px;color:var(--rust)}
.svc-card p{position:absolute;left:31px;width:370px;font-size:10px;line-height:18px;color:var(--muted)}
.svc-card .btn{position:absolute;left:29px;top:287px;width:87px;height:33px;line-height:33px;background:var(--rust);color:#fff}

/* 360 */
.view-band{left:0;top:2891px;width:848px;height:416px;background:var(--copper);border-top-right-radius:28px}
.view-band h2{position:absolute;left:195px;top:48px;font-family:var(--head);font-weight:300;font-size:36px;color:#fff}
.view-band p{position:absolute;left:197px;top:104px;font-size:9.5px;color:#f5e2d3}
.view-photo{left:222px;top:3048px;width:978px;height:476px;border-radius:4px;background:linear-gradient(180deg,#dcd8d2 0%,#f0eeeb 40%,#a9a39b 100%)}
.view-dot{left:728px;top:3455px;width:10px;height:10px;border-radius:50%;background:var(--copper)}

/* faq */
.faq-title{left:0;top:3605px;width:1200px;text-align:center;font-family:var(--head);font-size:36px;font-weight:400}
.faq-title span{color:var(--copper)}
.faq-rule{left:266px;width:666px;height:1px;background:var(--line)}
.faq-n{left:266px;font-size:12px;color:var(--copper)}
.faq-q{left:349px;font-size:13px;font-weight:500}
.faq-a{left:349px;top:3793px;width:520px;font-size:13px;line-height:19.5px;color:var(--muted)}
.faq-icon{left:895px;width:36px;height:36px;border-radius:50%;border:1px solid var(--copper);color:var(--copper);text-align:center;line-height:33px;font-size:18px}
.faq-house{left:0;top:3925px;width:231px;height:330px;background:linear-gradient(180deg,#9b9893 0%,#4d4a47 60%,#2f2c2a 100%)}

/* footer */
.footer{left:0;top:4255px;width:1200px;height:403px;background:var(--night);color:#fff}
.footer .brand{top:70px;color:#fff}
.footer .brand .dot{border-color:#fff}
.footer .rule{position:absolute;left:264px;top:172px;width:672px;height:1px;background:#4a4441}
.footer nav{position:absolute;left:0;top:203px;width:1200px;display:flex;justify-content:center;gap:38px;font-size:11px;color:#e6e1dd}
.footer .copy{position:absolute;left:264px;top:294px;font-size:10px;color:#d6d0cc}
.social{position:absolute;top:287px;width:31px;height:31px;border-radius:50%;background:#fff}
</style>
</head>
<body>

<header>
  <nav class="abs nav-links"><span>HOME</span><span>ABOUT</span><span>CONTACT</span><span>SERVICES</span></nav>
  <div class="abs brand"><i class="dot"></i><span class="name">WADE HOLLORAN</span><span class="sub">CUSTOM HOMES</span></div>
  <span class="abs nav-projects">PROJECTS</span>
  <span class="abs btn nav-quote">GET A QUOTES</span>
</header>

<section class="abs hero">
  <div class="abs ghost">Custom Homes</div>
  <div class="ph house" role="img" aria-label="Modern two-storey custom home at dusk"></div>
  <h1 class="abs">Wade Holloran<br>Custom Home<br>Build</h1>
  <p class="abs">Wade Holloran has been building stunning custom homes in the Indianapolis area for over 20 years.</p>
  <span class="abs btn b1">GET STARTED</span>
  <span class="abs btn b2">QUOTES</span>
</section>

<section>
  <h2 class="abs intro-title">Building beautiful<br>Custom Homes in Indianapolis</h2>
  <p class="abs intro-text">Wade Holloran has been building stunning custom homes in the Indianpolis area for over 20 years. As a small boutique building company we only build a handful of homes a year in order to offer our clients the personal attention that their homes deserve.</p>
  <div class="abs stat" style="left:190px"><div class="v">over 20</div><div class="l">Years Experience</div></div>
  <div class="abs stat-div" style="left:437px"></div>
  <div class="abs stat" style="left:495px"><div class="v">$2 to $10</div><div class="l">Million Budget</div></div>
  <div class="abs stat-div" style="left:746px"></div>
  <div class="abs stat" style="left:800px"><div class="v">High End</div><div class="l">Custom Builder</div></div>
  <div class="abs ghost2">High End Home Build</div>
  <div class="ph laptop" role="img" aria-label="Laptop showing a custom home website at sunset"></div>
</section>

<section class="abs projects">
  <h2 class="abs">Wade Holloran<br>Previous project</h2>
  <span class="abs arrow prev"><svg width="47" height="47" viewBox="0 0 47 47"><path d="M29 23.5H18M22 19l-4.5 4.5L22 28" stroke="#5a2a0f" stroke-width="1.4" fill="none"/></svg></span>
  <span class="abs arrow next"><svg width="47" height="47" viewBox="0 0 47 47"><path d="M18 23.5h11M25 19l4.5 4.5L25 28" stroke="#fff" stroke-width="1.4" fill="none"/></svg></span>

  <div class="card" style="left:0;top:285px">
    <div class="img" role="img" aria-label="Stone and timber home exterior at dusk" style="width:148px;height:363px;background:linear-gradient(180deg,#6b5040 0%,#b07a45 55%,#3f5a2c 100%)"></div>
    <span class="plus" style="left:110px;top:355px">+</span>
    <span class="t" style="left:5px;top:376px">case 08</span>
  </div>
  <div class="card" style="left:168px;top:285px">
    <div class="img" role="img" aria-label="Modern oak staircase with black railings" style="width:253px;height:363px;background:linear-gradient(160deg,#ecebe8 0%,#c9a57a 55%,#9b7448 100%)"></div>
    <span class="plus" style="left:226px;top:355px">+</span>
    <span class="t" style="left:15px;top:376px">Modern Stair case 08</span>
    <span class="s" style="left:15px;top:406px">Custom Build</span>
  </div>
  <div class="card" style="left:430px;top:249px">
    <div class="img" role="img" aria-label="White and walnut kitchen with pendant lights" style="width:340px;height:437px;background:linear-gradient(180deg,#f3f2ef 0%,#dcd8d2 45%,#8a5a34 75%,#3b2a20 100%)"></div>
    <span class="plus" style="left:300px;top:429px;background:var(--copper)">+</span>
    <span class="t" style="left:14px;top:449px">Modern Kitchen 08</span>
    <span class="s" style="left:14px;top:480px">Custom Build</span>
  </div>
  <div class="card" style="left:772px;top:285px">
    <div class="img" role="img" aria-label="Office cabin with wooden table and window view" style="width:262px;height:363px;background:linear-gradient(180deg,#d8dcdc 0%,#6e8a58 45%,#7a4a2a 80%,#3a2a20 100%)"></div>
    <span class="plus" style="left:226px;top:355px">+</span>
    <span class="t" style="left:14px;top:376px">Office Cabin 06</span>
    <span class="s" style="left:14px;top:406px">Custom Build</span>
  </div>
  <div class="card" style="left:1052px;top:285px">
    <div class="img" role="img" aria-label="Dining area with bar stools and screens" style="width:160px;height:363px;background:linear-gradient(180deg,#e9e6e2 0%,#8d7560 55%,#3c2e26 100%)"></div>
    <span class="t" style="left:10px;top:376px">Dinning Area Cab</span>
    <span class="s" style="left:10px;top:406px">Custom Build</span>
  </div>
</section>

<section>
  <div class="ph svc-bg" role="img" aria-label="Faint interior background"></div>
  <div class="ph svc-photo" role="img" aria-label="Light oak staircase with black railing"></div>
  <div class="abs svc-card">
    <h2>Wade Holloran Builder-<br>Construction<br>Services</h2>
    <p style="top:168px">Building beautiful custom homes in Indianapolis Budget&nbsp; $2 million to $10 million range.</p>
    <p style="top:212px">As a small boutique building company we only build a handful of homes a year in order to offer our clients the personal attention that their homes deserve.</p>
    <span class="btn">GET STARTED</span>
  </div>
</section>

<section>
  <div class="abs view-band">
    <h2>Wade Holloran 360° View</h2>
    <p>Building beautiful custom homes in Indianapolis Budget&nbsp; $2 million to $10 million range.</p>
  </div>
  <div class="ph view-photo" role="img" aria-label="Panoramic living room with stone columns and beamed ceiling"></div>
  <span class="abs view-dot"></span>
</section>

<section>
  <h2 class="abs faq-title">Frequently Asked <span>Questions</span></h2>
  <div class="ph faq-house" role="img" aria-label="Modern grey home facade"></div>
  <div class="abs faq-rule" style="top:3706px"></div>
  <span class="abs faq-n" style="top:3754px">01</span>
  <span class="abs faq-q" style="top:3752px">What services do you offer as a custom home builder?</span>
  <span class="abs faq-icon" style="top:3740px">×</span>
  <p class="abs faq-a">As a custom home builder, we offer a wide range of services including personalized home design, construction management, site preparation, interior and exterior finishing, and remodeling services. We strive to bring your dream home to life, tailored to your specific needs and preferences.</p>
  <div class="abs faq-rule" style="top:3894px"></div>
  <span class="abs faq-n" style="top:3938px">02</span>
  <span class="abs faq-q" style="top:3936px">How long does the custom home building process take?</span>
  <span class="abs faq-icon" style="top:3925px">+</span>
  <div class="abs faq-rule" style="top:3992px"></div>
  <span class="abs faq-n" style="top:4034px">03</span>
  <span class="abs faq-q" style="top:4032px">How much does it cost to build a custom home?</span>
  <span class="abs faq-icon" style="top:4022px">+</span>
  <div class="abs faq-rule" style="top:4089px"></div>
  <span class="abs faq-n" style="top:4132px">04</span>
  <span class="abs faq-q" style="top:4130px">Can I make changes to the design during the construction process?</span>
  <span class="abs faq-icon" style="top:4120px">+</span>
  <div class="abs faq-rule" style="top:4185px"></div>
</section>

<footer class="abs footer">
  <div class="abs brand"><i class="dot"></i><span class="name">WADE HOLLORAN</span><span class="sub">CUSTOM HOMES</span></div>
  <div class="rule"></div>
  <nav><span>Home</span><span>About Us</span><span>Contact Us</span><span>Services</span><span>Projects</span><span>Get Quotes</span></nav>
  <span class="copy">2023 © Wade Holloran All rights reserved</span>
  <span class="social" style="left:829px"></span>
  <span class="social" style="left:867px"></span>
  <span class="social" style="left:905px"></span>
</footer>

</body>
</html>
```